Maple Dawn Confections. We need a website as delcious as our chocolate.

I need a website to promote our humble chocolate business. We our proud of are chocolate because we use only our favorite ingredients. We believe in originality and complete enjoyment of our chocolates. I am looking for a sleek and smooth website. I would like to see typical pages such as contact information and an intro. I would like to have a product page, which can be easily updated with photos of new chocolate. I would also like to see a page where we can educate customers about chocolate. This might be tricky but I would like our customers to leave the site knowing they are getting great chocolate! I have a logo and general color scheme, which I will try to upload somewhere. I looking for an original and exciting website.
Updates

Websites we like:

1. http://www.corvel-amand.example/ (looks really good)

2. http://www.tilvarocacao.example/

uploaded logo !

Target Market(s)

People who enjoy chocolate.

Industry/Entity Type

Business

Requirements
Must have
• User Friendly
Page were pictures of new chocolate can be easily updated.

Nice to have
• Calming and appetizing music
Section where recent tweets can show up on the site.

```html
<!DOCTYPE html>
<html lang="en">
<head>
<meta charset="utf-8">
<title>Maple Dawn Confections</title>
<link rel="stylesheet" href="https://fonts.googleapis.com/css2?family=Arimo:wght@400;700&display=swap">
<style>
  :root {
    --ink-deep: #120a07;
    --panel-edge: #9a8a78;
    --orange-text: #e4892e;
    --pink-head: #e2346c;
    --nav-top: #b9580c;
    --nav-bottom: #4e1f04;
    --nav-divider: #2a1003;
    --footer-link: #a47c64;
    --field-border: #e07a18;
    --button-top: #f07a22;
    --button-bottom: #b24408;
  }
  * { box-sizing: border-box; margin: 0; padding: 0; }
  html, body { width: 1080px; height: 1200px; overflow: hidden; }
  body {
    font-family: "Arimo", Arial, sans-serif;
    background: var(--ink-deep);
    position: relative;
  }
  .backdrop {
    position: absolute; inset: 0;
    background:
      radial-gradient(ellipse 420px 260px at 120px 1130px, rgba(196,110,50,.75), transparent 70%),
      radial-gradient(ellipse 360px 300px at 540px 1200px, rgba(150,80,40,.55), transparent 70%),
      radial-gradient(ellipse 380px 320px at 900px 380px, rgba(120,70,40,.55), transparent 70%),
      radial-gradient(ellipse 300px 260px at 260px 360px, rgba(110,64,36,.6), transparent 70%),
      radial-gradient(ellipse 260px 200px at 1000px 1050px, rgba(150,80,40,.45), transparent 70%),
      linear-gradient(160deg, #1a0d08 0%, #2c170c 45%, #1c0e08 100%);
  }
  .page {
    position: absolute; left: 61px; top: 67px; width: 958px; height: 1066px;
    border: 1px solid var(--panel-edge);
    box-shadow: 0 0 14px rgba(0,0,0,.7);
    background: rgba(16,8,5,.55);
  }
  .site-header { position: relative; height: 137px; background: rgba(14,7,4,.92); }
  .brand {
    position: absolute; left: 14px; top: 44px;
    color: var(--orange-text); font-weight: 400; font-size: 26px; letter-spacing: .5px;
    display: flex; align-items: center; gap: 10px;
  }
  .brand-mark { width: 14px; height: 14px; background: var(--orange-text); }
  .social { position: absolute; top: 16px; left: 840px; display: flex; gap: 12px; }
  .social span { width: 19px; height: 19px; border-radius: 3px; background: #8a8a8a; }
  .social span:nth-child(1) { background: #4aa8d8; }
  .social span:nth-child(2) { background: #3b5b98; }
  .social span:nth-child(3) { background: #7aa83a; }
  .search { position: absolute; left: 709px; top: 89px; display: flex; gap: 11px; }
  .search-field {
    width: 163px; height: 27px; border: 1px solid var(--field-border);
    border-radius: 3px; background: #0a0503;
  }
  .search-go {
    width: 44px; height: 27px; border-radius: 3px; color: #fff; font-size: 14px;
    display: flex; align-items: center; justify-content: center;
    background: linear-gradient(var(--button-top), var(--button-bottom));
  }
  .main-nav {
    display: flex; height: 50px;
    background: linear-gradient(var(--nav-top), #7a3306 55%, var(--nav-bottom));
  }
  .main-nav a {
    flex: 1; display: flex; align-items: center; justify-content: center;
    color: #fff; text-decoration: none; font-size: 18px;
    border-right: 2px solid var(--nav-divider);
  }
  .main-nav a:last-child { border-right: 0; }
  .hero {
    margin-top: 6px; height: 361px;
    border-top: 1px solid #6a5a50; border-bottom: 1px solid #6a5a50;
    background:
      radial-gradient(ellipse 180px 140px at 110px 150px, rgba(120,70,60,.7), transparent 70%),
      radial-gradient(ellipse 260px 200px at 820px 200px, rgba(170,90,80,.6), transparent 70%),
      radial-gradient(ellipse 200px 160px at 420px 200px, rgba(150,130,130,.45), transparent 70%),
      linear-gradient(90deg, #2e1a18 0%, #5a3e3c 35%, #4a2c2c 55%, #6a2c3c 75%, #7a3a40 100%);
  }
  .content { position: relative; height: 462px; }
  .col-left, .col-right { position: absolute; top: 0; }
  .col-left { left: 11px; width: 562px; }
  .col-right { left: 606px; width: 341px; }
  .content h2, .content h3, .content p, .read-more { position: absolute; left: 0; }
  .content h2 { color: var(--pink-head); font-size: 17px; font-weight: 400; letter-spacing: .3px; }
  .content h3 { color: var(--pink-head); font-size: 14px; font-weight: 700; letter-spacing: .5px; left: 2px; }
  .content p {
    width: 100%; color: var(--orange-text); font-size: 13px; line-height: 20px;
    letter-spacing: 1.1px; text-align: justify;
  }
  .read-more {
    width: 74px; height: 17px; border-radius: 4px; color: #fff;
    font-size: 11px; font-weight: 700; display: flex; align-items: center; justify-content: center;
    background: linear-gradient(#c8620e, #5a2404);
    box-shadow: 0 1px 2px rgba(0,0,0,.6);
  }
  .site-footer {
    position: absolute; left: 0; right: 0; bottom: 0; height: 46px;
    background: linear-gradient(#7c3a08, #3c1804);
    display: flex; align-items: center; justify-content: center;
    color: var(--footer-link); font-size: 16px; letter-spacing: .3px;
  }
  .site-footer a { color: var(--footer-link); text-decoration: none; }
</style>
</head>
<body>
  <div class="backdrop" role="img" aria-label="Soft blurred close-up of chocolates in warm brown and amber tones"></div>
  <div class="page">
    <header class="site-header">
      <div class="brand"><span class="brand-mark"></span>Maple Dawn Confections</div>
      <div class="social" aria-label="Social links"><span></span><span></span><span></span></div>
      <div class="search"><div class="search-field"></div><div class="search-go">GO</div></div>
    </header>
    <nav class="main-nav">
      <a href="#">Home</a><a href="#">About us</a><a href="#">Products</a><a href="#">Shop online</a><a href="#">Contact us</a>
    </nav>
    <div class="hero" role="img" aria-label="Photo of assorted gourmet chocolates and truffles in paper cups"></div>
    <main class="content">
      <section class="col-left">
        <h2 style="top:17px">Welcome to our website</h2>
        <p style="top:48px">Maple Dawn's mission is to be a respected leader in the gourmet deserts industry. We aim to create a unique experience during the consumption of our delights. We promise to provide an appetizing and diversified selection. We guarantee our customers real value to fulfill their expectations.</p>
        <h3 style="top:151px">Bussiness Stategy</h3>
        <p style="top:182px">Our business exists purely online. We are able to print on our chocolates, and the internet has afforded us the opportunity to personalize our messages according to our customer's preferences.</p>
        <h3 style="top:263px">Our Services</h3>
        <p style="top:292px">A company that makes homemade chocolate. Our competitive positioning stems from our benefit positioning which is ,Giving the customers the freedom to personalise their own orders.Build lasting and profitable customer relationships by providing personalized chocolate delights.Business that need the chocolate for their meetings and conferences as well as social events</p>
        <a class="read-more" style="top:421px">Read more</a>
      </section>
      <section class="col-right">
        <h2 style="top:17px">Our Vision</h2>
        <p style="top:49px">Maple Dawn vision is to expand further then just producing chocolates. The expansion would entail creating all sorts of deserts, ranging from cakes to cookies. Also Maple Dawn would like to expand into being and online-offline business, by opening up an actual store.</p>
        <a class="read-more" style="top:190px">Read more</a>
        <h2 style="top:225px">Product details</h2>
        <p style="top:260px">Maple Dawn vision is to expand further then just producing chocolates. The expansion would entail creating all sorts of deserts, ranging from cakes to cookies. Also Maple Dawn would like to expand into being and online-offline business, by opening up an actual store. The expansion would entail creating all sorts.</p>
        <a class="read-more" style="top:422px">Read more</a>
      </section>
    </main>
    <footer class="site-footer">
      <a href="#">Home</a>&nbsp;|&nbsp;<a href="#">About us</a>&nbsp;|&nbsp;<a href="#">Products</a>&nbsp;|&nbsp;<a href="#">Shop onlone</a>&nbsp;|&nbsp;<a href="#">contact us</a>
    </footer>
  </div>
</body>
</html>
```